Kestrel Bathrooms

Fix our flyer add as the one we got made has the wrong phone number on it would like different photos on it

Want it to Stand out and be in your face!

I will attach our logo
phone number is 0487265903
Email is Miles@kestrelbathrooms.com.au

happy to keep all prices the same

If you can make it better happy to tip $$

```html
<!DOCTYPE html>
<html lang="en">
<head>
<meta charset="utf-8">
<title>Kestrel Bathrooms Flyer</title>
<link rel="stylesheet" href="https://fonts.googleapis.com/css2?family=Montserrat:wght@400;600;700;800;900&display=swap">
<style>
:root{
  --blue:#1a6fc0;
  --sky:#3fa4f0;
  --ink:#1b1b1b;
  --black:#000;
  --white:#fff;
  --grey:#444;
  --dark-card:#262626;
}
*{box-sizing:border-box;margin:0;padding:0}
html,body{width:942px;height:1200px;overflow:hidden;background:var(--white)}
body{font-family:"Montserrat",sans-serif;color:var(--ink)}
.flyer{position:relative;width:942px;height:1200px;overflow:hidden;background:var(--white)}
.hero-photo{position:absolute;left:0;top:0;width:942px;height:504px;
  background:linear-gradient(120deg,#e8dccb 0%,#c9a77c 35%,#efe6d8 60%,#8c8276 100%)}
.hero-shapes{position:absolute;left:0;top:0}
.brand-name{position:absolute;left:66px;top:226px;width:390px;display:flex;align-items:center;gap:16px;
  color:var(--blue);font-weight:800;font-size:52px;line-height:1.02;text-transform:uppercase;letter-spacing:1px}
.brand-name .mark{width:28px;height:28px;background:var(--blue);flex:none}
.pkg-frame{position:absolute;background:var(--white);border-radius:14px}
.photo{position:absolute;border-radius:14px}
.photo-main{left:182px;top:444px;width:280px;height:188px;background:linear-gradient(135deg,#1f4a3a,#6b6a5e 55%,#d9d4cc)}
.photo-ensuite{left:42px;top:658px;width:280px;height:188px;background:linear-gradient(90deg,#141414,#d9dde0 45%,#f2f2f2 60%,#8a6b4c)}
.photo-laundry{left:182px;top:871px;width:280px;height:187px;background:linear-gradient(135deg,#8a7565,#d7d2cb 50%,#3a3a3a)}
.pkg{position:absolute;border-radius:10px;padding:12px 12px 0 12px}
.pkg-blue{background:var(--blue);color:var(--white)}
.pkg-dark{background:var(--dark-card);color:var(--white)}
.pkg-title{font-weight:900;font-size:24px;line-height:.86;text-transform:uppercase}
.price-box{position:absolute;left:8px;right:8px;bottom:8px;background:var(--white);border-radius:6px;padding:4px 8px 0}
.price-label{font-size:12.5px;font-weight:600;color:var(--ink)}
.price{font-size:42px;font-weight:900;line-height:1;color:var(--ink);letter-spacing:-.5px}
.pkg-dark .price-label,.pkg-dark .price{color:var(--blue)}
.save-tag{position:absolute;background:var(--black);color:var(--white);font-weight:800;font-size:11px;
  padding:3px 8px;border-radius:8px;white-space:nowrap}
.save-tag.blue{background:var(--blue)}
.local-banner{position:absolute;left:511px;top:558px;width:431px;height:84px;background:var(--blue);
  color:var(--white);font-weight:700;font-size:24px;letter-spacing:3px;line-height:1.35;padding:10px 0 0 20px}
.licence{position:absolute;left:514px;top:676px}
.licence .kicker{color:var(--blue);font-weight:800;font-size:22px}
.licence h1{font-weight:900;font-size:44px;line-height:1.08;color:var(--ink);margin-top:2px}
.built{position:absolute;left:514px;top:826px}
.built h2{color:var(--blue);font-weight:900;font-size:33px}
.built p{font-size:16.5px;color:var(--grey);margin-top:-2px}
.services{position:absolute;left:514px;top:888px;width:400px;display:grid;grid-template-columns:212px 188px;row-gap:9px;list-style:none}
.services li{display:flex;align-items:center;gap:7px;font-weight:700;font-size:19.5px;color:var(--ink)}
.services li svg{flex:none}
.fixtures{position:absolute;left:515px;top:1028px;font-size:17px;color:var(--grey)}
.terms{position:absolute;left:598px;top:1080px;font-size:9.5px;color:var(--ink)}
.contact-bar{position:absolute;left:0;top:1100px;width:942px;height:100px;display:flex}
.call{width:462px;background:var(--sky);display:flex;align-items:center;padding-left:42px;gap:16px;color:var(--white)}
.web{flex:1;background:var(--black);display:flex;align-items:center;padding-left:27px;gap:20px;color:var(--white)}
.icon-tile{width:55px;height:55px;background:var(--white);border-radius:7px;display:flex;align-items:center;justify-content:center;flex:none}
.call-label{font-weight:700;font-size:21px;line-height:1}
.call-number{font-weight:900;font-size:45px;line-height:1}
.web-lines{font-weight:700;font-size:18.5px;line-height:1.35}
.web-lines .hl{color:var(--sky)}
</style>
</head>
<body>
<div class="flyer">
  <div class="hero-photo" role="img" aria-label="Photo of a modern bathroom with stone-tiled wall, arched mirror, vessel basin and vanity with towels"></div>

  <svg class="hero-shapes" width="942" height="1100" viewBox="0 0 942 1100" aria-hidden="true">
    <polygon points="34,198 161,118 470,183 470,504 34,504" fill="#0b0b0b" opacity=".93"/>
    <path d="M0,504 H770 C840,504 905,530 942,640 V1100 H0 Z" fill="#fff"/>
  </svg>

  <div class="brand-name"><span class="mark"></span><span>Kestrel<br>Bathrooms</span></div>

  <div class="pkg-frame" style="left:34px;top:426px;width:436px;height:210px"></div>
  <div class="photo photo-main" role="img" aria-label="Photo of a bathroom vanity with green tiled wall and white basin"></div>
  <div class="pkg pkg-blue" style="left:42px;top:462px;width:232px;height:158px">
    <div class="pkg-title">Main<br>Bathroom<br>Package</div>
    <div class="price-box"><div class="price-label">Price Starts From</div><div class="price">$18,900</div></div>
  </div>
  <div class="save-tag" style="left:141px;top:455px">SAVE UP TO $4,000</div>

  <div class="photo photo-ensuite" role="img" aria-label="Photo of an ensuite with freestanding bath beside tall windows"></div>
  <div class="pkg pkg-dark" style="left:228px;top:675px;width:234px;height:154px;padding-top:20px">
    <div class="pkg-title">Ensuite<br>Package</div>
    <div class="price-box"><div class="price-label">Price Starts From</div><div class="price">$14,900</div></div>
  </div>
  <div class="save-tag blue" style="left:328px;top:668px">SAVE UP TO $4,000</div>

  <div class="photo photo-laundry" role="img" aria-label="Photo of a laundry with front-loading washer and benchtop basin"></div>
  <div class="pkg pkg-blue" style="left:42px;top:894px;width:232px;height:153px;padding-top:26px">
    <div class="pkg-title">Laundry<br>Package</div>
    <div class="price-box"><div class="price-label">Price Starts From</div><div class="price">$9,900</div></div>
  </div>
  <div class="save-tag" style="left:141px;top:888px">SAVE UP TO $4,000</div>

  <div class="local-banner">ILLAWARRA BASED<br>AND FAMILY OPERATED</div>

  <div class="licence">
    <div class="kicker">KESTREL BATHROOMS</div>
    <h1>FULLY LICENSED<br>&amp; INSURED</h1>
  </div>

  <div class="built">
    <h2>BUILT TO LAST</h2>
    <p>Your local renovation specialist</p>
  </div>

  <ul class="services">
    <li><svg width="16" height="16" viewBox="0 0 16 16"><circle cx="8" cy="8" r="6.5" fill="none" stroke="#1a6fc0" stroke-width="2"/><path d="M5 8l2.2 2.2L13 4" fill="none" stroke="#1a6fc0" stroke-width="2.2"/></svg>Demolition</li>
    <li><svg width="16" height="16" viewBox="0 0 16 16"><circle cx="8" cy="8" r="6.5" fill="none" stroke="#1a6fc0" stroke-width="2"/><path d="M5 8l2.2 2.2L13 4" fill="none" stroke="#1a6fc0" stroke-width="2.2"/></svg>Waterproofing</li>
    <li><svg width="16" height="16" viewBox="0 0 16 16"><circle cx="8" cy="8" r="6.5" fill="none" stroke="#1a6fc0" stroke-width="2"/><path d="M5 8l2.2 2.2L13 4" fill="none" stroke="#1a6fc0" stroke-width="2.2"/></svg>Electrical</li>
    <li><svg width="16" height="16" viewBox="0 0 16 16"><circle cx="8" cy="8" r="6.5" fill="none" stroke="#1a6fc0" stroke-width="2"/><path d="M5 8l2.2 2.2L13 4" fill="none" stroke="#1a6fc0" stroke-width="2.2"/></svg>Plumbing</li>
    <li><svg width="16" height="16" viewBox="0 0 16 16"><circle cx="8" cy="8" r="6.5" fill="none" stroke="#1a6fc0" stroke-width="2"/><path d="M5 8l2.2 2.2L13 4" fill="none" stroke="#1a6fc0" stroke-width="2.2"/></svg>Carpentry</li>
    <li><svg width="16" height="16" viewBox="0 0 16 16"><circle cx="8" cy="8" r="6.5" fill="none" stroke="#1a6fc0" stroke-width="2"/><path d="M5 8l2.2 2.2L13 4" fill="none" stroke="#1a6fc0" stroke-width="2.2"/></svg>Tiling</li>
    <li style="grid-column:1 / span 2"><svg width="16" height="16" viewBox="0 0 16 16"><circle cx="8" cy="8" r="6.5" fill="none" stroke="#1a6fc0" stroke-width="2"/><path d="M5 8l2.2 2.2L13 4" fill="none" stroke="#1a6fc0" stroke-width="2.2"/></svg>Design Consultation</li>
  </ul>

  <div class="fixtures">Organisation and delivery of all fixtures</div>
  <div class="terms">*Terms and conditions apply and onsite quote required.</div>

  <div class="contact-bar">
    <div class="call">
      <div class="icon-tile">
        <svg width="34" height="34" viewBox="0 0 24 24"><path d="M6.6 2.5l3 3.2-1.8 2.2c1 2.3 2.9 4.2 5.3 5.3l2.2-1.8 3.2 3-1.5 3.1c-7.4-.6-13-6.2-13.6-13.6z" fill="none" stroke="#222" stroke-width="1.5" stroke-linejoin="round"/></svg>
      </div>
      <div>
        <div class="call-label">CALL US AT</div>
        <div class="call-number">0487 265 903</div>
      </div>
    </div>
    <div class="web">
      <div class="icon-tile">
        <svg width="34" height="34" viewBox="0 0 24 24"><circle cx="11" cy="11" r="8" fill="none" stroke="#222" stroke-width="1.6"/><ellipse cx="11" cy="11" rx="3.5" ry="8" fill="none" stroke="#222" stroke-width="1.4"/><path d="M3 11h16M4.5 7h13M4.5 15h13" stroke="#222" stroke-width="1.3"/><path d="M13 13l8 3-3.5 1.2L16 21z" fill="#3fa4f0"/></svg>
      </div>
      <div class="web-lines">
        <div>www.<span class="hl">kestrel</span>bathrooms.com.au</div>
        <div>Miles@kestrel<span class="hl">bathrooms</span>.com.au</div>
      </div>
    </div>
  </div>
</div>
</body>
</html>
```